We currently have a good logo and we want business cards that can display our logo but also represent our industry - telecom construction - We are a construction company specializing in telecom construction such as installation of fiber optic cable throughout cities and across the country. Nationwide services
We are large enough to handle most any project yet small enough to be a flexible partner and resource.

Target Market(s)

U.S. based telecom carriers and providers

Industry/Entity Type

Construction

Contact Information for Business Card

Business cards should include our logo, phone number and website address. Also, including some information as to our core services would be good.

Colors

Designer to choose colors to be used in the design.

Requirements
Must have
• Colors based on logo
• Must use our logo
• Logo, name, email, website address, phone number
• Tovasco Conduit
• Brent Halvik
• Director of Business Development
• (555) 271-0386
• www.TVSQ-example.com
Nice to have
• Construction services including:
• Small Cell Construction
• Boring/Drilling
• Plowing / Trenching
• Conduit installation
• Fiber pulling
• splicing
• building entries
• Aerial construction
• Aerial Make Ready
• Make Ready Engineering
Should not have
• We are open to ideas

```html
<!DOCTYPE html>
<html lang="en">
<head>
<meta charset="utf-8">
<title>Tovasco Conduit – Business Cards</title>
<link href="https://fonts.googleapis.com/css2?family=Montserrat:wght@400;800&family=Open+Sans:wght@400;600&family=Roboto+Condensed:wght@400&display=swap" rel="stylesheet">
<style>
  :root {
    --backdrop: #2a2b2d;
    --card: #050607;
    --brand-blue: #1a7fd8;
    --name-blue: #1f5fcf;
    --muted-grey: #8a8d90;
    --rule-grey: #5c5f62;
    --list-white: #f2f2f2;
  }
  * { margin: 0; padding: 0; box-sizing: border-box; }
  html, body { width: 1200px; height: 900px; overflow: hidden; }
  body {
    background: radial-gradient(ellipse at 60% 20%, #3a3b3e 0%, var(--backdrop) 55%, #151617 100%);
    position: relative;
  }
  .card {
    position: absolute;
    left: 250px;
    width: 700px;
    height: 390px;
    background: var(--card);
    box-shadow: 0 12px 30px rgba(0,0,0,.6);
  }
  .card--front { top: 40px; }
  .card--back { top: 470px; }

  .brand-name {
    font-family: "Montserrat", sans-serif;
    font-weight: 800;
    color: var(--brand-blue);
    letter-spacing: .5px;
    line-height: 1.05;
  }

  /* Front */
  .card--front .brand-name {
    position: absolute;
    left: 60px; top: 140px;
    font-size: 40px;
    width: 290px;
  }
  .front-divider {
    position: absolute;
    left: 370px; top: 70px;
    width: 1px; height: 250px;
    background: var(--rule-grey);
  }
  .services {
    position: absolute;
    left: 395px; top: 70px;
    font-family: "Open Sans", sans-serif;
  }
  .services__intro {
    font-size: 14px;
    color: var(--muted-grey);
    margin-bottom: 4px;
  }
  .services__list { list-style: none; }
  .services__list li {
    font-size: 16px;
    font-weight: 600;
    color: var(--list-white);
    line-height: 21px;
    padding-left: 18px;
    position: relative;
  }
  .services__list li::before {
    content: "";
    position: absolute;
    left: 0; top: 7px;
    width: 8px; height: 8px;
    border-radius: 50%;
    background: var(--list-white);
  }

  /* Back */
  .card--back .brand-name {
    position: absolute;
    left: 70px; top: 45px;
    font-size: 34px;
    width: 260px;
  }
  .person {
    position: absolute;
    left: 70px; top: 150px;
  }
  .person__name {
    font-family: "Montserrat", sans-serif;
    font-weight: 800;
    font-size: 30px;
    color: var(--name-blue);
    letter-spacing: 1px;
  }
  .person__title {
    font-family: "Roboto Condensed", sans-serif;
    font-size: 20px;
    color: var(--muted-grey);
  }
  .accent-line {
    position: absolute;
    left: 70px; top: 238px;
    width: 590px; height: 4px;
    background: var(--brand-blue);
    border-radius: 2px;
  }
  .contacts {
    position: absolute;
    left: 60px; top: 262px;
    list-style: none;
    font-family: "Montserrat", sans-serif;
    font-size: 21px;
    color: var(--muted-grey);
  }
  .contacts li {
    display: flex;
    align-items: center;
    gap: 12px;
    line-height: 33px;
  }
  .contacts svg { width: 20px; height: 20px; flex: none; }
</style>
</head>
<body>

<section class="card card--front">
  <div class="brand-name">Tovasco Conduit</div>
  <div class="front-divider"></div>
  <div class="services">
    <p class="services__intro">Construction services including:</p>
    <ul class="services__list">
      <li>Small Cell Construction</li>
      <li>Boring/Drilling</li>
      <li>Plowing / Trenching</li>
      <li>Conduit installation</li>
      <li>Fiber pulling</li>
      <li>splicing</li>
      <li>building entries</li>
      <li>Aerial construction</li>
      <li>Aerial Make Ready</li>
      <li>Make Ready Engineering</li>
    </ul>
  </div>
</section>

<section class="card card--back">
  <div class="brand-name">Tovasco Conduit</div>
  <div class="person">
    <div class="person__name">BRENT HALVIK</div>
    <div class="person__title">Director of Business Development</div>
  </div>
  <div class="accent-line"></div>
  <ul class="contacts">
    <li>
      <svg viewBox="0 0 20 20" fill="none" stroke="var(--brand-blue)" stroke-width="1.6">
        <circle cx="10" cy="10" r="8.5"/>
        <path d="M7 6.5c0 4 2.5 6.5 6.5 6.5l.8-1.8-2-1-1 .9c-1.2-.5-2-1.3-2.5-2.5l.9-1-1-2z" fill="var(--brand-blue)" stroke="none"/>
      </svg>
      (555) 271-0386
    </li>
    <li>
      <svg viewBox="0 0 20 20" fill="none" stroke="var(--brand-blue)" stroke-width="1.6">
        <rect x="2" y="4.5" width="16" height="11"/>
        <path d="M2 4.5l8 6.5 8-6.5"/>
      </svg>
      info@brenthalvik-example.com
    </li>
    <li>
      <svg viewBox="0 0 20 20" fill="none" stroke="var(--brand-blue)" stroke-width="1.6">
        <circle cx="10" cy="10" r="8.5"/>
        <ellipse cx="10" cy="10" rx="3.8" ry="8.5"/>
        <path d="M1.5 10h17M3 5.5h14M3 14.5h14"/>
      </svg>
      www.TVSQ-example.com
    </li>
  </ul>
</section>

</body>
</html>
```